World travel poster - I want to remember where I've been!

I would like a poster for me to print and keep in my home as a record of my world travels. It must look like a mechanical sign in an airport (see picture for example) However I am flexible with exact layout, if you'd like to add images used to enhance poster etc. I have also uploaded some pictures from my travels if you would like to use some or all of them. They are named according to location.

Poster must include:
USA 2003
Malaysia 2006
Thailand 2007
Italy 2009
India, Vietnam, Hong Kong 2010
Bali 2011
Malaysia 2012
Singapore 2012
Vietnam, Cambodia, Laos 2013
Europe 2015

and the quote:

"The world is a book and those who do not travel read only one page."
― Severin of Tallowmere
Updates

Hi there. I have uploaded some photos of my travels to possibly use in my poster. They are named according to location. I haven't decided if I prefer the originial layout or with images, so please post both for me to consider. Thanks so much for your time to consider my project.

Target Market(s)

Something to catch the eye of visitors and remind me of my adventures.
A classic piece that is a conversation starter.

Industry/Entity Type

Airport

Other font styles liked:
• Airport mechanical font

Requirements
Must have
• Some lettering like a mechanical airport board (see image attached for example).
Dimensions that are easy to print - either A3, or a long/narrow poster.
Nice to have
• A splash of colour or an image, maybe the words 'arrivals' or 'departures'

Use of some of my pictures if it doesn't look too busy.
Should not have
• Anything too over the top.

```html
<!DOCTYPE html>
<html lang="en">
<head>
<meta charset="utf-8">
<title>Departures – Travel Record</title>
<link rel="stylesheet" href="https://fonts.googleapis.com/css2?family=Arimo:wght@700&family=Barlow+Condensed:wght@500&display=swap">
<style>
  :root {
    --paper: #ffffff;
    --board: #2a3739;
    --board-edge: #1b2426;
    --panel: #334244;
    --row: #364547;
    --tile: #3a494b;
    --tile-gap: #161e20;
    --split: #1c2527;
    --flap-yellow: #f6e200;
    --ink-white: #ffffff;
    --badge-red: #e8161b;
    --badge-red-light: #ff5a5a;
  }
  * { box-sizing: border-box; margin: 0; padding: 0; }
  html, body {
    width: 1200px; height: 967px; overflow: hidden;
    background: var(--paper);
  }
  .poster {
    position: relative; width: 1200px; height: 967px;
    background: var(--paper);
  }
  .board {
    position: absolute; left: 0; top: 47px; width: 1200px; height: 920px;
    background: var(--board);
  }
  .header-panel {
    position: absolute; left: 16px; top: 21px; width: 1172px; height: 121px;
    background: linear-gradient(var(--panel) 0 49.5%, var(--board-edge) 49.5% 50.5%, var(--panel) 50.5%);
    border: 2px solid var(--board-edge); border-radius: 4px;
  }
  .plane-badge {
    position: absolute; left: 86px; top: 13px; width: 96px; height: 96px;
    border-radius: 10px;
    background: linear-gradient(var(--badge-red-light) 0 30%, var(--badge-red) 30%);
  }
  .plane-badge svg { width: 96px; height: 96px; display: block; }
  .board-title {
    position: absolute; left: 258px; top: 10px;
    font-family: "Arimo", Arial, sans-serif; font-weight: 700;
    font-size: 109px; line-height: 100px; color: var(--ink-white);
    letter-spacing: -1px;
  }
  .flight-list {
    position: absolute; left: 0; top: 155px; width: 1200px;
  }
  .flight-row {
    height: 62.4px; padding: 5.5px 0 0 19.5px;
    background: linear-gradient(var(--row) 0 95%, var(--board-edge) 95%);
  }
  .flaps {
    display: grid;
    grid-template-columns: repeat(28, 37.5px);
    column-gap: 4.1px;
    height: 51px;
    background:
      linear-gradient(transparent 0 49%, var(--split) 49% 51%, transparent 51%),
      repeating-linear-gradient(90deg, var(--tile) 0 37.5px, var(--tile-gap) 37.5px 41.6px);
    width: 1161px;
  }
  .flaps span {
    font-family: "Barlow Condensed", "Arial Narrow", sans-serif; font-weight: 500;
    font-size: 55px; line-height: 51px; text-align: center;
    color: var(--flap-yellow);
  }
  .flaps .year { grid-column: 25 / span 4; display: grid; grid-template-columns: repeat(4, 37.5px); column-gap: 4.1px; }
  .quote-panel {
    position: absolute; left: 16px; top: 780px; width: 1172px; height: 121px;
    background: linear-gradient(var(--panel) 0 49.5%, var(--board-edge) 49.5% 50.5%, var(--panel) 50.5%);
    border: 2px solid var(--board-edge); border-radius: 4px;
    font-family: "Arimo", Arial, sans-serif; font-weight: 700; color: var(--ink-white);
  }
  .quote-text { position: absolute; left: 0; width: 100%; top: 20px; text-align: center; font-size: 29.5px; }
  .quote-author { position: absolute; right: 24px; top: 59px; font-size: 29.5px; }
</style>
</head>
<body>
<div class="poster">
  <div class="board">
    <div class="header-panel">
      <div class="plane-badge">
        <svg viewBox="0 0 96 96" aria-hidden="true">
          <path fill="#fff" d="M48 8c3 0 4 5 4 10v20l34 16v8l-34-8v22l9 7v5l-13-3-13 3v-5l9-7V54l-34 8v-8l34-16V18c0-5 1-10 4-10z"/>
        </svg>
      </div>
      <h1 class="board-title">DEPARTURES</h1>
    </div>

    <div class="flight-list">
      <div class="flight-row"><div class="flaps"><span>U</span><span>S</span><span>A</span><div class="year"><span>2</span><span>0</span><span>0</span><span>3</span></div></div></div>
      <div class="flight-row"><div class="flaps"><span>M</span><span>A</span><span>L</span><span>A</span><span>Y</span><span>S</span><span>I</span><span>A</span><div class="year"><span>2</span><span>0</span><span>0</span><span>6</span></div></div></div>
      <div class="flight-row"><div class="flaps"><span>T</span><span>H</span><span>A</span><span>I</span><span>L</span><span>A</span><span>N</span><span>D</span><div class="year"><span>2</span><span>0</span><span>0</span><span>7</span></div></div></div>
      <div class="flight-row"><div class="flaps"><span>I</span><span>T</span><span>A</span><span>L</span><span>Y</span><div class="year"><span>2</span><span>0</span><span>0</span><span>9</span></div></div></div>
      <div class="flight-row"><div class="flaps"><span>I</span><span>N</span><span>D</span><span>I</span><span>A</span><span></span><span>V</span><span>I</span><span>E</span><span>T</span><span>N</span><span>A</span><span>M</span><span></span><span>H</span><span>O</span><span>N</span><span>G</span><span></span><span>K</span><span>O</span><span>N</span><span>G</span><div class="year"><span>2</span><span>0</span><span>1</span><span>0</span></div></div></div>
      <div class="flight-row"><div class="flaps"><span>B</span><span>A</span><span>L</span><span>I</span><div class="year"><span>2</span><span>0</span><span>1</span><span>1</span></div></div></div>
      <div class="flight-row"><div class="flaps"><span>M</span><span>A</span><span>L</span><span>A</span><span>Y</span><span>S</span><span>I</span><span>A</span><div class="year"><span>2</span><span>0</span><span>1</span><span>2</span></div></div></div>
      <div class="flight-row"><div class="flaps"><span>S</span><span>I</span><span>N</span><span>G</span><span>A</span><span>P</span><span>O</span><span>R</span><span>E</span><div class="year"><span>2</span><span>0</span><span>1</span><span>2</span></div></div></div>
      <div class="flight-row"><div class="flaps"><span>V</span><span>I</span><span>E</span><span>T</span><span>N</span><span>A</span><span>M</span><span></span><span>C</span><span>A</span><span>M</span><span>B</span><span>O</span><span>D</span><span>I</span><span>A</span><span></span><span>L</span><span>A</span><span>O</span><span>S</span><div class="year"><span>2</span><span>0</span><span>1</span><span>3</span></div></div></div>
      <div class="flight-row"><div class="flaps"><span>E</span><span>U</span><span>R</span><span>O</span><span>P</span><span>E</span><div class="year"><span>2</span><span>0</span><span>1</span><span>5</span></div></div></div>
    </div>

    <div class="quote-panel">
      <p class="quote-text">"The world is a book and those who do not travel read only one page."</p>
      <p class="quote-author">— Severin of Tallowmere</p>
    </div>
  </div>
</div>
</body>
</html>
```